Harbourline Refrigeration business card design

We would like a new design for our business card as we have a new logo.
We need generic business card to give our customers with our office details - with the option of making it individualized for each manager

Target Market(s)

Companies and homeowners

Industry/Entity Type

Air Conditioning

Contact Information for Business Card

We are not sure if we want single or double sided it will depend on the design we choose

Colors
33a6d7
0255a3

Requirements
Must have
• Logo
• phone: (08) 8721 5940
• email: harbourserve@tealnet.example
• website: www.harbourlinerefrigeration.example
• AU61420
• BLD472913
Nice to have
• Address - Shed 5/284 Tallis Rd, Whyalla Norrie SA 5608

```html
<!DOCTYPE html>
<html lang="en">
<head>
<meta charset="utf-8">
<title>Harbourline Refrigeration – Business Card</title>
<link href="https://fonts.googleapis.com/css2?family=Lato:wght@400;700&family=Oswald:wght@500&display=swap" rel="stylesheet">
<style>
  :root {
    --navy: #0a3f86;
    --brand-blue: #0255a3;
    --sky: #33a6d7;
    --ink: #1e1e1e;
    --rule: #b9b9b9;
    --backdrop: #2b2b2b;
    --paper: #ffffff;
  }
  * { margin: 0; padding: 0; box-sizing: border-box; }
  html, body { width: 1200px; height: 1200px; overflow: hidden; }
  body {
    background: var(--backdrop);
    position: relative;
    font-family: "Lato", sans-serif;
  }
  .card {
    position: absolute;
    top: 310px;
    width: 366px;
    height: 594px;
  }
  .card--front {
    left: 233px;
    background: var(--paper);
    text-align: center;
    color: var(--ink);
  }
  .card--back {
    left: 628px;
    background: linear-gradient(135deg, #1a6fb8 0%, #2f93d2 48%, #1c6db5 100%);
    color: #fff;
  }
  .brand {
    position: absolute;
    left: 0; right: 0;
    display: flex;
    align-items: center;
    justify-content: center;
    gap: 12px;
  }
  .brand__dot {
    width: 22px; height: 22px;
    border-radius: 50%;
  }
  .brand__name {
    font-family: "Lato", sans-serif;
    font-weight: 700;
    font-size: 30px;
    line-height: 1.05;
    text-align: left;
  }
  .card--front .brand { top: 135px; }
  .card--front .brand__dot { background: var(--sky); }
  .card--front .brand__name { color: var(--brand-blue); }
  .card--back .brand { top: 395px; left: 30px; right: 30px; justify-content: flex-end; }
  .card--back .brand__dot { background: #fff; }
  .card--back .brand__name { color: #fff; }

  .person { position: absolute; top: 300px; left: 0; right: 0; }
  .person__name {
    font-family: "Oswald", sans-serif;
    font-weight: 500;
    font-size: 27px;
    color: var(--navy);
    letter-spacing: 0.2px;
  }
  .person__role { font-size: 17px; color: var(--sky); margin-top: 1px; }
  .divider {
    position: absolute; left: 88px; width: 190px;
    height: 1px; background: var(--rule);
  }
  .divider--top { top: 368px; }
  .address {
    position: absolute; top: 387px; left: 0; right: 0;
    font-size: 17px; line-height: 22px;
  }
  .icon-row {
    position: absolute; top: 448px; left: 88px; right: 88px;
    display: flex; align-items: center; gap: 3px;
  }
  .icon-row__line { flex: 1; height: 1px; background: var(--rule); }
  .icon-row svg { width: 25px; height: 25px; display: block; }
  .contact {
    position: absolute; top: 480px; left: 0; right: 0;
    font-size: 17px; line-height: 22px;
  }
  .card--back .pattern {
    position: absolute; inset: 0 0 auto 0; height: 330px;
    background: radial-gradient(ellipse at 60% 55%, rgba(120,200,240,0.35), rgba(255,255,255,0) 65%);
  }
  .licences {
    position: absolute; top: 530px; left: 60px; right: 60px;
    text-align: center;
    font-size: 17px; letter-spacing: 0.3px;
  }
</style>
</head>
<body>
  <section class="card card--front">
    <div class="brand">
      <span class="brand__dot"></span>
      <span class="brand__name">Harbourline<br>Refrigeration</span>
    </div>
    <div class="person">
      <div class="person__name">DARA WHITFIELD</div>
      <div class="person__role">Manager</div>
    </div>
    <div class="divider divider--top"></div>
    <div class="address">Shed 5/284 Tallis Rd<br>Whyalla Norrie SA 5608</div>
    <div class="icon-row">
      <span class="icon-row__line"></span>
      <svg viewBox="0 0 24 24" aria-label="Phone"><circle cx="12" cy="12" r="12" fill="#0a3f86"/><path d="M6 10c0-2 3-3 6-3s6 1 6 3l-2 1-1-2h-6l-1 2zM8 12h8l1 5H7z" fill="#fff"/></svg>
      <svg viewBox="0 0 24 24" aria-label="Email"><circle cx="12" cy="12" r="12" fill="#0a3f86"/><rect x="6" y="8" width="12" height="8" fill="#fff"/><path d="M6 8l6 5 6-5" fill="none" stroke="#0a3f86" stroke-width="1.2"/></svg>
      <svg viewBox="0 0 24 24" aria-label="Website"><circle cx="12" cy="12" r="12" fill="#0a3f86"/><circle cx="12" cy="12" r="6" fill="none" stroke="#fff" stroke-width="1.5"/><path d="M6 12h12M12 6c-3 3-3 9 0 12M12 6c3 3 3 9 0 12" fill="none" stroke="#fff" stroke-width="1.2"/></svg>
      <span class="icon-row__line"></span>
    </div>
    <div class="contact">
      (08) 8721 5940<br>
      harbourserve@tealnet.example<br>
      www.harbourlinerefrigeration.example
    </div>
  </section>

  <section class="card card--back">
    <div class="pattern" role="img" aria-label="Faint large decorative brand pattern"></div>
    <div class="brand">
      <span class="brand__dot"></span>
      <span class="brand__name">Harbourline<br>Refrigeration</span>
    </div>
    <div class="licences">AU61420&nbsp;&nbsp;|&nbsp;&nbsp;BLD472913</div>
  </section>
</body>
</html>
```